Fence Flyer to Attract More Sales During Winter

We need a new flyer made that we can distribute to residential mailboxes. The flyer is to promote our Frostline Picket Days. We like simply designs, and we would like the flyer to showcase a lot of our fence photos. More of our photos are online at our website at www.getbramblerail.com - our new address needs to also be featured on the flyer - 436 Quillen rd, Monroe, NC 28117. I do want the words "FROSTLINE PICKET DAYS" to be dominate on the flyer with the description "Wood fences starting at $12/FT!" Please look through our Facebook page and our website to gather more photos or information. We are flexible on colors, nothing to fancy - simple flyer design please.

Target Market(s)

Residential homeowners that need a new fence to enclose their yard for safety, security or decorative

Industry/Entity Type

Residential Construction

Font styles to use
Sans Serif

Colors

Designer to choose colors to be used in the design.

Requirements
Must have
• Frostline Picket Days
• Contact information for the business
• "Come visit our outdoor showroom, open 24/7!"
Nice to have
• Photos of our fences - you can find more on our website at www.GetBrambleRail.com or Facebook.com/MeadowlarkRailGPV
Should not have
• Flashy designs

```html
<!DOCTYPE html>
<html lang="en">
<head>
<meta charset="utf-8">
<title>Frostline Picket Days Flyer</title>
<link href="https://fonts.googleapis.com/css2?family=Poppins:wght@400;500;600;800&family=Yellowtail&family=Oswald:wght@700&display=swap" rel="stylesheet">
<style>
  :root {
    --page: #f1f2f3;
    --navy: #1f3350;
    --navy-deep: #10243f;
    --orange: #e8912f;
    --white: #ffffff;
    --black: #0b0b0b;
    --logo-blue: #3a86c8;
  }
  * { box-sizing: border-box; margin: 0; padding: 0; }
  html, body { width: 1200px; height: 1200px; overflow: hidden; background: var(--page); }
  body { display: flex; align-items: center; justify-content: center; font-family: "Poppins", sans-serif; }

  .flyer {
    position: relative; width: 896px; height: 1160px; overflow: hidden;
    background: var(--navy);
    box-shadow: 0 14px 40px rgba(0,0,0,.18);
  }
  .hero-photo {
    position: absolute; left: 0; top: 0; width: 100%; height: 820px;
    background:
      radial-gradient(ellipse at 30% 25%, rgba(60,85,115,.55), transparent 60%),
      linear-gradient(160deg, #263d5c 0%, #1f3350 55%, #1b2e4a 100%);
  }

  .brand-card {
    position: absolute; left: 36px; top: 70px; width: 258px; height: 108px;
    background: var(--white); padding: 16px 18px;
    display: flex; align-items: center; gap: 14px;
  }
  .brand-mark { width: 26px; height: 26px; border-radius: 50%; background: var(--orange); flex: none; }
  .brand-name { font-weight: 600; font-size: 19px; color: var(--logo-blue); line-height: 1.1; }
  .brand-phone { font-weight: 800; font-size: 18px; color: var(--black); margin-top: 3px; }
  .brand-tagline { font-size: 8px; font-style: italic; color: #333; margin-top: 3px; }

  .showroom {
    position: absolute; right: 40px; top: 96px; display: flex; align-items: baseline; gap: 14px;
  }
  .showroom-text { color: var(--orange); font-weight: 500; font-size: 20px; }
  .showroom-hours { color: var(--white); font-weight: 600; font-size: 34px; letter-spacing: 2px; }

  .headline { position: absolute; left: 0; right: 0; top: 250px; text-align: center; }
  .headline-script {
    font-family: "Yellowtail", cursive; color: var(--white); font-size: 150px; line-height: 1;
    padding-left: 40px;
  }
  .headline-bold {
    font-family: "Poppins", sans-serif; font-weight: 800; color: var(--orange);
    font-size: 132px; line-height: 1.05; letter-spacing: 1px; margin-top: 10px; padding-left: 70px;
  }

  .offer-band {
    position: absolute; left: 0; right: 0; top: 812px; height: 48px; background: var(--orange);
    display: flex; align-items: center; padding-left: 44px;
  }
  .offer-text { color: var(--navy-deep); font-weight: 800; font-size: 18px; letter-spacing: 9px; }

  .gallery { position: absolute; left: 0; right: 0; top: 860px; height: 200px; display: flex; }
  .gallery-photo { flex: 1; }
  .photo-gate { background: linear-gradient(180deg, #3f5a2c 0%, #8d8150 55%, #b79a68 100%); }
  .photo-yard { background: linear-gradient(180deg, #8fb0cf 0%, #5f7d3c 35%, #c7b184 70%, #6b5637 100%); }
  .photo-side { background: linear-gradient(180deg, #dfe3e6 0%, #c9b88e 40%, #b8a276 100%); }
  .photo-door { background: linear-gradient(180deg, #9fbedc 0%, #d6c59b 35%, #c4ae7c 100%); }

  .price-badge {
    position: absolute; left: 640px; top: 720px; width: 240px; height: 240px; border-radius: 50%;
    background: var(--navy-deep);
    border: 6px solid #c6ccd4;
    display: flex; flex-direction: column; align-items: center; justify-content: center;
    color: var(--white);
  }
  .price-amount { font-family: "Oswald", sans-serif; font-weight: 700; font-size: 96px; line-height: 1; }
  .price-unit { font-weight: 500; font-size: 26px; letter-spacing: 1px; margin-top: 4px; }

  .footer {
    position: absolute; left: 0; right: 0; bottom: 0; height: 100px; background: var(--black);
    color: var(--white); text-align: center;
    display: flex; flex-direction: column; justify-content: center;
    font-size: 19px; letter-spacing: 1.5px; line-height: 1.45;
  }
</style>
</head>
<body>
  <main class="flyer">
    <div class="hero-photo" role="img" aria-label="Dark blue tinted photo of a wooden picket fence covered in snow"></div>

    <div class="brand-card">
      <span class="brand-mark"></span>
      <div>
        <div class="brand-name">Bramble Rail Fence</div>
        <div class="brand-phone">704-555-0163</div>
        <div class="brand-tagline">"Because Good Fences Make Good Neighbors"</div>
      </div>
    </div>

    <p class="showroom">
      <span class="showroom-text">Come visit our outdoor showroom, open</span>
      <span class="showroom-hours">24/7!</span>
    </p>

    <h1 class="headline">
      <div class="headline-script">Frostline</div>
      <div class="headline-bold">PICKET<br>DAYS</div>
    </h1>

    <div class="offer-band"><span class="offer-text">WOOD FENCES STARTING AT</span></div>

    <div class="gallery">
      <div class="gallery-photo photo-gate" role="img" aria-label="Wooden arched gate beside a split rail fence"></div>
      <div class="gallery-photo photo-yard" role="img" aria-label="Privacy fence along a garden bed with shrubs"></div>
      <div class="gallery-photo photo-side" role="img" aria-label="Scalloped wood fence beside a white house"></div>
      <div class="gallery-photo photo-door" role="img" aria-label="Wooden fence gate with black hardware"></div>
    </div>

    <div class="price-badge">
      <span class="price-amount">$12</span>
      <span class="price-unit">per ft</span>
    </div>

    <footer class="footer">
      <span>www.getbramblerail.com</span>
      <span>Address : 436 Quillen rd, Monroe, NC 28117</span>
    </footer>
  </main>
</body>
</html>
```